Monthly Mailed Newsletter/Magazine for Medical Spa

Every month we send out a mailed newsletter/magazine to our visitors from the previous month. We made a sample newsletter/magazine as a guideline of what we are looking for. We need a designer to make a simple and clean design layout.

- Attached is our sample design that has all the content we want to use.
- Newsletter/magazine is 8 pages total.
- Size of each page is 8.5 inches in width by 11 inches in height.
- Content and images can be located here: https://files.vornacloud.net/shared/8kqTRw3ZpLmX2vNcA7yHd5EbJ0sUgFo4e?view=open

The following will give you an idea of our brand presentation.
Our website is: www.GlowDermaClinic.com
Our Instagram; @glowdermaclinic
Our Facebook: www.socialtreo.com/glowdermaclinic

Target Market(s)

Women 25 - 45

Industry/Entity Type

Beauty

Font styles to use
Other font styles liked:
• Josefins Sans Bold & Lato

Colors
f78f20
ffffff

Requirements
Must have
• - Our Logo
- Our tagline: YOUR SKIN DESERVES IT!
- Address and contact information for our locations
- Our color scheme: Black and #FAA641
- Heading font is Josefin Sans Bold
- Paragraph font is Lato
- Our website address: www.GlowDermaClinic.com

```html
<!DOCTYPE html>
<html lang="en">
<head>
<meta charset="utf-8">
<title>Glow Derma Clinic — Monthly Newsletter</title>
<link rel="stylesheet" href="https://fonts.googleapis.com/css2?family=Josefin+Sans:ital,wght@0,400;0,600;0,700;1,600&family=Lato:ital,wght@0,400;0,700;0,900;1,400&display=swap">
<style>
:root{
  --orange:#f6a23d;
  --orange-deep:#f08f24;
  --ink:#1c1c1c;
  --grey-text:#444;
  --panel:#efefef;
  --cream:#f6f1ea;
  --stage:#5d5e66;
  --white:#ffffff;
  --skin-a:#dcbba3;
  --skin-b:#8f6a57;
}
*{box-sizing:border-box;margin:0;padding:0}
html,body{width:1200px;height:3600px;overflow:hidden}
body{background:var(--stage);font-family:"Lato",sans-serif;color:var(--ink);position:relative}
.spread{position:absolute;left:40px;top:342px;display:grid;grid-template-columns:540px 540px;gap:39px 40px}
.page{position:relative;width:540px;height:699px;overflow:hidden;background:var(--white)}
h1,h2,h3,h4{font-family:"Josefin Sans",sans-serif;font-weight:700}
.photo{position:absolute;background:linear-gradient(140deg,var(--skin-a),var(--skin-b))}
.photo.cool{background:linear-gradient(150deg,#c9ccd0,#5b5f66)}
.photo.warm{background:linear-gradient(150deg,#ead2bd,#b58a6b)}
.photo.dark{background:linear-gradient(150deg,#9d8478,#3a302c)}
.photo.round{border-radius:50%;border:5px solid var(--white)}
.folio{position:absolute;bottom:10px;width:28px;height:28px;border-radius:50%;background:var(--ink);color:var(--white);font:700 9px/28px "Lato",sans-serif;text-align:center}
.folio.left{left:12px}.folio.right{right:12px}
.body-text{font-size:8.2px;line-height:1.45;color:var(--grey-text)}
.body-text p+p{margin-top:6px}
.q-head{font-family:"Josefin Sans",sans-serif;font-weight:700;font-size:11px;color:var(--ink);margin:10px 0 5px;display:flex;align-items:center;gap:6px}
.q-head::before{content:"";width:6px;height:6px;border-radius:50%;background:var(--orange)}
.brand{font-family:"Josefin Sans",sans-serif;font-weight:700;color:var(--ink);display:flex;align-items:center;gap:8px}
.brand .dot{width:14px;height:14px;border-radius:50%;background:var(--orange);flex:none}

/* back cover */
.back-cover{background:var(--orange);color:var(--white)}
.back-cover .tagline{position:absolute;top:186px;width:100%;text-align:center;font-size:50px;line-height:1;letter-spacing:1px}
.back-cover .rule{position:absolute;left:0;top:411px;width:100%;height:3px;background:var(--white)}
.seal{position:absolute;left:178px;top:322px;width:184px;height:184px;border-radius:50%;background:var(--white);box-shadow:0 0 0 6px var(--orange),0 0 0 9px var(--white);display:flex;flex-direction:column;align-items:center;justify-content:center;gap:8px}
.seal .name{font-family:"Josefin Sans",sans-serif;font-weight:700;font-size:21px;line-height:1.05;text-align:center;color:var(--ink)}
.seal .dot{width:22px;height:22px;border-radius:50%;background:var(--orange)}
.location{position:absolute;top:434px;width:150px;font-size:10.5px;line-height:1.4}
.location.left{left:26px}
.location.right{right:26px;text-align:right}
.location .city{font-family:"Josefin Sans",sans-serif;font-weight:700;font-size:17px;margin-bottom:14px;letter-spacing:.5px}
.location .line{display:flex;gap:6px;align-items:flex-start;margin-bottom:20px}
.location.right .line{flex-direction:row-reverse}
.location svg{flex:none;margin-top:1px}
.social{position:absolute;left:250px;top:594px;display:flex;gap:8px}
.social span{width:16px;height:16px;border:2px solid var(--white);border-radius:3px}
.site-pill{position:absolute;left:112px;top:652px;width:316px;height:32px;border-radius:16px;background:var(--white);color:var(--orange);font:700 15px/33px "Josefin Sans",sans-serif;text-align:center}

/* front cover */
.cover .brand{position:absolute;right:26px;top:30px;font-size:19px}
.cover-ring{position:absolute;left:24px;top:94px;width:492px;height:492px;border-radius:50%;border:2px solid var(--orange)}
.cover-disc{position:absolute;left:34px;top:104px;width:472px;height:472px;border-radius:50%;overflow:hidden;background:var(--white)}
.cover-disc .photo{left:0;top:0;width:100%;height:292px}
.cover-disc .thanks{position:absolute;top:300px;width:100%;text-align:center;color:var(--orange);font-size:50px;line-height:1}
.cover-disc .band{position:absolute;top:352px;left:0;width:100%;height:94px;background:var(--orange);color:var(--white);text-align:center;font:700 27px/1 "Josefin Sans",sans-serif;padding-top:14px}
.cover-disc .issue{position:absolute;left:161px;top:404px;width:150px;height:150px;border-radius:50%;background:var(--white);text-align:center;padding-top:20px;color:var(--orange);font:600 13px/1.05 "Josefin Sans",sans-serif}
.teasers{position:absolute;left:22px;top:604px;width:496px;display:grid;grid-template-columns:1fr 1fr 1fr}
.teaser{text-align:center;padding:0 8px}
.teaser+.teaser{border-left:2px solid var(--orange)}
.teaser h4{font-size:11.5px;line-height:1.15;text-transform:uppercase}
.teaser p{font-size:9px;line-height:1.25;color:var(--grey-text);margin-top:3px}
.cover .foot-bar{position:absolute;left:0;bottom:0;width:100%;height:14px;background:var(--orange)}

/* contents */
.contents .strip{position:absolute;left:430px;top:0;width:110px;height:100%;background:var(--orange)}
.contents .panel{position:absolute;left:66px;top:148px;width:364px;height:512px;background:var(--panel)}
.page-title{position:absolute;left:58px;top:32px;font-size:42px;line-height:1.02;letter-spacing:.5px}
.page-title .accent{color:var(--orange)}
.toc-item{position:absolute;left:40px;width:300px;display:flex;gap:14px;align-items:flex-start}
.toc-item .num{width:44px;height:44px;border-radius:50%;background:var(--orange);color:var(--white);font:700 19px/46px "Josefin Sans",sans-serif;text-align:center;flex:none;border:3px solid var(--white)}
.toc-item h3{font-size:13px;line-height:1.05;text-transform:uppercase;padding-top:4px}
.toc-item p{font-size:8.5px;line-height:1.35;color:var(--grey-text);margin-top:3px}

/* promotion */
.promo .strip{position:absolute;right:0;top:0;width:34px;height:100%;background:var(--orange)}
.promo .topline{position:absolute;left:0;top:0;width:100%;height:6px;background:var(--orange)}
.promo .page-title{left:32px;top:30px;font-size:40px}
.promo .intro{position:absolute;left:32px;top:140px;width:290px;font-size:9.5px;line-height:1.45;color:var(--grey-text);border-top:1px solid #ddd;padding-top:10px}
.promo .intro b{color:var(--orange)}
.price-list{position:absolute;left:32px;top:218px;width:280px;list-style:none}
.price-list li{margin-bottom:9px;padding-left:16px;position:relative;font-size:9.4px;line-height:1.4}
.price-list li::before{content:"";position:absolute;left:0;top:2px;width:8px;height:8px;border-radius:50%;background:var(--orange)}
.price-list h4{font-size:9.5px;color:var(--orange);text-transform:uppercase;font-weight:600;letter-spacing:.3px}

/* hair removal */
.hair .top{position:absolute;left:0;top:0;width:100%;height:275px;background:var(--orange)}
.kicker{position:absolute;left:30px;top:12px;background:var(--white);padding:5px 14px 3px;font:600 15px/1 "Josefin Sans",sans-serif;letter-spacing:.5px}
.hair h2{position:absolute;left:32px;top:50px;color:var(--white);font-size:31px;line-height:1.05;letter-spacing:.5px}
.hair h2 .big{font-size:48px}
.hair .text{position:absolute;left:28px;top:388px;width:484px}
.hair .foot-bar{position:absolute;left:0;bottom:0;width:100%;height:6px;background:var(--orange)}

/* shaving quote */
.shave .block{position:absolute;left:0;top:0;width:338px;height:290px;background:var(--orange)}
.shave .quote{position:absolute;left:32px;top:40px;width:282px;height:390px;background:var(--cream);border:1px solid #cfc8bf;padding:44px 40px;font:600 17px/1.32 "Josefin Sans",sans-serif}
.shave .quote p+p{margin-top:20px}
.shave .text{position:absolute;left:30px;top:446px;width:296px}

/* lumitox tips */
.tips .side-label{position:absolute;left:10px;top:20px;width:196px;background:var(--ink);color:var(--white);padding:10px 12px 8px;font:700 15px/1.1 "Josefin Sans",sans-serif}
.tip{position:absolute;left:10px;width:196px;height:140px;border-top:2px dashed var(--orange);padding-top:8px}
.tip h4{font-size:12px;text-transform:uppercase}
.tip h4 span{color:var(--orange);font-size:10px;margin-right:4px}
.tip .photo{left:4px;top:34px;width:86px;height:86px}
.tip p{margin-left:96px;margin-top:6px;font-size:8px;line-height:1.35;color:var(--grey-text)}
.tips .hero{position:absolute;left:220px;top:0;width:320px;height:422px;background:var(--orange)}
.tips .hero .photo{left:38px;top:28px;width:250px;height:250px}
.tips .hero h2{position:absolute;left:0;top:298px;width:100%;text-align:center;color:var(--white);font-size:29px;line-height:1.02}
.tips .text{position:absolute;left:234px;top:438px;width:286px}

/* closing page */
.closing .lead{position:absolute;top:30px;width:100%;text-align:center;color:var(--orange);font:italic 600 20px/1.3 "Josefin Sans",sans-serif}
.closing .sign{position:absolute;top:104px;width:100%;display:flex;justify-content:center;align-items:center;gap:6px;font-size:12px}
.closing .sign .dot{width:10px;height:10px;border-radius:50%;background:var(--orange)}
.closing .band{position:absolute;left:0;top:180px;width:100%;height:220px;background:var(--orange)}
.closing .faint{position:absolute;left:450px;top:240px;width:90px;height:90px;border-radius:50%;background:rgba(255,255,255,.35)}
.closing .col{position:absolute;top:418px;width:236px}
.closing .col h4{font-size:10.5px;line-height:1.2;margin-bottom:6px}
.closing .recommend{position:absolute;left:22px;top:560px;width:236px;border:2px solid var(--orange);padding:12px 14px;font-size:8.3px;line-height:1.4;color:var(--grey-text)}
.closing .recommend p+p{margin-top:8px}
.closing .foot-bar{position:absolute;left:0;bottom:0;width:100%;height:6px;background:var(--orange)}
</style>
</head>
<body>
<main class="spread">

  <!-- back cover -->
  <section class="page back-cover">
    <h2 class="tagline">YOUR SKIN<br>DESERVES IT</h2>
    <div class="rule"></div>
    <div class="seal">
      <span class="dot"></span>
      <span class="name">Glow<br>Derma Clinic</span>
    </div>
    <div class="location left">
      <div class="city">MESAVIEW</div>
      <div class="line"><svg width="10" height="12" viewBox="0 0 10 12"><path d="M5 0a4 4 0 0 0-4 4c0 3 4 8 4 8s4-5 4-8a4 4 0 0 0-4-4zm0 5.5A1.5 1.5 0 1 1 5 2.5a1.5 1.5 0 0 1 0 3z" fill="#fff"/></svg><span>1480 East Saguaro Lane,<br>Suite 210, Mesaview,<br>AZ 85990</span></div>
      <div class="line"><svg width="10" height="10" viewBox="0 0 10 10"><path d="M2 0l2 2.5-1 1.2a6 6 0 0 0 3.3 3.3l1.2-1L10 8 8.6 9.6C4.5 10 0 5.5.4 1.4z" fill="#fff"/></svg><span>Call/Text: 520-555-0148</span></div>
      <div class="line"><svg width="11" height="9" viewBox="0 0 11 9"><rect x=".5" y=".5" width="10" height="8" fill="none" stroke="#fff"/><path d="M.5.5l5 4 5-4" fill="none" stroke="#fff"/></svg><span>hello@glowdermaclinic.com</span></div>
    </div>
    <div class="location right">
      <div class="city">DUNEPORT, AZ</div>
      <div class="line"><svg width="10" height="12" viewBox="0 0 10 12"><path d="M5 0a4 4 0 0 0-4 4c0 3 4 8 4 8s4-5 4-8a4 4 0 0 0-4-4zm0 5.5A1.5 1.5 0 1 1 5 2.5a1.5 1.5 0 0 1 0 3z" fill="#fff"/></svg><span>3625 Desert Palm Drive,<br>Suite B, Duneport,<br>AZ 85399</span></div>
      <div class="line"><svg width="10" height="10" viewBox="0 0 10 10"><path d="M2 0l2 2.5-1 1.2a6 6 0 0 0 3.3 3.3l1.2-1L10 8 8.6 9.6C4.5 10 0 5.5.4 1.4z" fill="#fff"/></svg><span>Call/Text: 928-555-0172</span></div>
      <div class="line"><svg width="11" height="9" viewBox="0 0 11 9"><rect x=".5" y=".5" width="10" height="8" fill="none" stroke="#fff"/><path d="M.5.5l5 4 5-4" fill="none" stroke="#fff"/></svg><span>hello@glowdermaclinic.com</span></div>
    </div>
    <div class="social" aria-label="Social media: @glowdermaclinic"><span></span><span></span></div>
    <div class="site-pill">www.GlowDermaClinic.com</div>
  </section>

  <!-- front cover -->
  <section class="page cover">
    <div class="brand"><span class="dot"></span>Glow Derma Clinic</div>
    <div class="cover-ring"></div>
    <div class="cover-disc">
      <div class="photo warm" role="img" aria-label="Client relaxing on a treatment bed during a laser session with a clinician"></div>
      <h1 class="thanks">THANK YOU</h1>
      <div class="band">For Visiting Us</div>
      <div class="issue">NOV2021<br>ISSUE #02</div>
    </div>
    <div class="teasers">
      <div class="teaser"><h4>Is at-home<br>laser hair removal<br>effective?</h4><p>Unbiased professional opinions<br>to zap away your FAQs.</p></div>
      <div class="teaser"><h4>How does<br>Lumitox work?</h4><p>Lumitox reduces<br>dynamic wrinkles</p></div>
      <div class="teaser"><h4>How can<br>I be aware of<br>false claim?</h4><p>When in doubt, ask certified<br>skincare professionals.</p></div>
    </div>
    <div class="foot-bar"></div>
  </section>

  <!-- contents -->
  <section class="page contents">
    <div class="strip"></div>
    <div class="panel"></div>
    <h2 class="page-title">THE<br><span class="accent">CONTENT</span></h2>
    <div class="photo round warm" style="left:346px;top:34px;width:172px;height:172px" role="img" aria-label="Gloved hand holding a laser handpiece to skin"></div>
    <div class="photo round" style="left:346px;top:268px;width:172px;height:172px" role="img" aria-label="Woman touching her cheek and checking her skin"></div>
    <div class="photo round cool" style="left:346px;top:490px;width:172px;height:172px" role="img" aria-label="Clinician wearing a face mask"></div>
    <div class="toc-item" style="top:168px"><span class="num">03</span><div><h3>November 2020<br>Promotion</h3><p>Don't miss out on end of the year promotions.</p></div></div>
    <div class="toc-item" style="top:272px"><span class="num">04</span><div><h3>Is at-home laser hair<br>removal effective?</h3><p>Here are some unbiased professional opinions<br>to zap away your FAQs.</p></div></div>
    <div class="toc-item" style="top:371px"><span class="num">05</span><div><h3>How to make Lumitox<br>results last longer?</h3><p>We sought advice board-certified advice from<br>professionals to bring you the answer.</p></div></div>
    <div class="toc-item" style="top:475px"><span class="num">06</span><div><h3>Use sunscreen, eat right,<br>stress less, hydrate</h3><p>Drink sufficient fluids and protect your skin<br>with a broad-spectrum sunscreen.</p></div></div>
    <div class="toc-item" style="top:584px"><span class="num">07</span><div><h3>How can I be aware<br>of false claims?</h3><p>When in doubt, ask certified skincare<br>professionals.</p></div></div>
    <span class="folio left">02</span>
  </section>

  <!-- promotion -->
  <section class="page promo">
    <div class="topline"></div>
    <div class="strip"></div>
    <h2 class="page-title">NOVEMBER<br><span class="accent">PROMOTION</span></h2>
    <p class="intro">The following promotions are available to our active members. An annual payment of <b>$9.99</b> gives you access to reduced pricing, member-only packages, payment plans, and rewards.</p>
    <div class="photo round dark" style="left:338px;top:34px;width:172px;height:172px" role="img" aria-label="Smiling clinic team member in dark scrubs"></div>
    <div class="photo round" style="left:338px;top:268px;width:172px;height:172px" role="img" aria-label="Facial microneedling treatment close-up"></div>
    <div class="photo round cool" style="left:338px;top:490px;width:172px;height:172px" role="img" aria-label="Treatment room with laser equipment"></div>
    <ul class="price-list">
      <li><h4>Laser hair removal</h4>1 Area - 6 pack - 294<br>2 Areas - 6 pack - 510<br>3 Areas - 6 pack - 726</li>
      <li><h4>IPL: Photofacial</h4>1 Session - $89<br>2 Sessions - $178</li>
      <li><h4>Microneedling</h4>1 Treatment - 150<br>2 Treatments - 290<br>With PRP - Add $99 per treatment</li>
      <li><h4>Lumitox &amp; filler happy hour</h4>20 units - 160<br>40 units - 320<br>Lip Filler - 399*<br>Cheek Filler - 490*<br>tax not included<br>November Promotions</li>
      <li><h4>Chemical peels &amp; more</h4>Pure Layer Peel + Kit - 109<br>Clarion Revive Peel + Kit - 160<br>AeroGlow + Retinol - $109</li>
      <li><h4>Resurfacing laser</h4>Single treatment - $600</li>
      <li><h4>Tattoo removal</h4>6 Sessions on small area - 534</li>
    </ul>
    <span class="folio right">03</span>
  </section>

  <!-- hair removal -->
  <section class="page hair">
    <div class="top"></div>
    <span class="kicker">THE UNBIASED TRUTH</span>
    <h2>IS AT-HOME<br>LASER HAIR REMOVAL<br><span class="big">EFFECTIVE?</span></h2>
    <div class="photo round warm" style="left:19px;top:198px;width:154px;height:154px" role="img" aria-label="Woman using an at-home laser device on her underarm"></div>
    <div class="photo round warm" style="left:193px;top:198px;width:154px;height:154px" role="img" aria-label="Smiling woman raising her arm after hair removal"></div>
    <div class="photo round cool" style="left:365px;top:198px;width:154px;height:154px" role="img" aria-label="Laser device gliding over a leg"></div>
    <div class="text body-text">
      <div class="q-head">How does laser hair removal work?</div>
      <p>Laser hair removal uses a concentrated beam of light to target melanin, also known as your natural pigment. Through this, the follicle that produces hair is damaged. This delays the future growth of hairs.</p>
      <div class="q-head">Do at-home laser hair removal gadgets work?</div>
      <p>Dermatology professionals answer this popular question with a very cautionary yes. Dr. Arun Malhotra says results vary according to individuals. Success depends on the contrast between your hair and skin color. Light skin and dark hair produce the best outcomes, while other combinations can prove ineffective. At-home products are more suitable for use on smaller areas such as the lip and underarms. They can also help with maintenance after in-office treatments, keeping stray regrowth under control between visits to the clinic.</p>
      <p>Always read the device guidance carefully before the first use. Test a small patch of skin, keep the lens clean, and never treat the same spot twice in one session. Stop at once if you notice redness that lasts longer than a day.</p>
      <p>Consistency matters more than intensity. Most devices suggest weekly sessions for the first two months, then monthly touch-ups. Keep a simple log of dates and settings so you can share it with your provider at your next appointment.</p>
    </div>
    <div class="foot-bar"></div>
    <span class="folio left">04</span>
  </section>

  <!-- shaving quote -->
  <section class="page shave">
    <div class="block"></div>
    <div class="quote"><p>"I love how prickly your skin feels."<br>said no one ever!</p><p>Did you know that the average modern woman shaves 7,718 times in one lifetime?"</p></div>
    <div class="photo warm" style="left:340px;top:0;width:200px;height:274px" role="img" aria-label="Woman in a towel turban with shaving foam on her face"></div>
    <div class="photo" style="left:340px;top:282px;width:200px;height:168px;background:linear-gradient(140deg,#e8c3b4,#b36f66)" role="img" aria-label="Close-up of skin with razor irritation"></div>
    <div class="photo warm" style="left:340px;top:459px;width:200px;height:200px" role="img" aria-label="Smooth legs stretched out on a bright floor"></div>
    <div class="text body-text">
      <div class="q-head">Are there any risks involved?</div>
      <p>There is a risk of hyperpigmentation and skin damage if the device is used inappropriately. Although so, Velvorine Skin Studio esthetician Mara Quinlan claims that approved home devices are generally safe. She said that they are however not as effective as in-office treatments. It is important to thoroughly understand the product before using it. For example, most products are not suitable for breastfeeding or pregnant mothers.</p>
      <div class="q-head">A last word of advice?</div>
      <p>No matter which you choose, it's important to avoid tweezing hairs, tanning lotions, antibiotics, and retinoids two weeks prior and post-treatment. Life is too short for everyone to be at war with hair woes. If you don't use it, just lose it!</p>
    </div>
    <span class="folio right">05</span>
  </section>

  <!-- lumitox tips -->
  <section class="page tips">
    <div class="side-label">SIMPLE WAYS TO<br>PROLONG LUMITOX</div>
    <div class="tip" style="top:88px"><h4><span>1.</span>Use sunscreen</h4><div class="photo round warm" role="img" aria-label="Woman in a sun hat on the beach"></div><p>Sun damage can cause premature wrinkles. Drink sufficient fluids and protect your skin with a broad-spectrum sunscreen.</p></div>
    <div class="tip" style="top:240px"><h4><span>2.</span>Eat right</h4><div class="photo round" style="background:linear-gradient(140deg,#f2c24b,#c8402c)" role="img" aria-label="Bowl of fresh fruit"></div><p>Avoid highly processed foods and eat a balanced diet. Fresh fruits and vegetables contain antioxidants great for skin health.</p></div>
    <div class="tip" style="top:392px"><h4><span>3.</span>Buff your skincare routine</h4><div class="photo round cool" role="img" aria-label="Skincare bottles and jars"></div><p>A religious skincare routine is the holy-grail to healthy skin. Incorporate skin peels and collagen to speed up cell re-generation for a more youthful tone.</p></div>
    <div class="tip" style="top:552px"><h4><span>4.</span>Daily musts</h4><div class="photo round cool" role="img" aria-label="Glass of water"></div><p>Hydrate &amp; seek ways to stress less</p></div>
    <div class="hero"><div class="photo round" role="img" aria-label="Woman with curly hair touching her forehead"></div><h2>CAN YOU MAKE<br>YOUR LUMITOX<br>LAST LONGER?</h2></div>
    <div class="text body-text">
      <p>Aging is a fact of life but looking your age isn't! "Keep calm and get Lumitox", they say. But what if the recent lockdown has rendered both impossible? Is there a way you can prolong the magical effects of expensive injections during the syringe hiatus? We sought advice from professionals to bring you the answer.</p>
      <p>How does Lumitox work? It reduces dynamic wrinkles but not ones caused by UV damage or gravity. A purified protein is injected in minute amounts to block signals from nerves and cause paralysis. Results only last for about 3 months depending on administration.</p>
      <p><b>Is it possible to make Lumitox &amp; fillers last longer?</b></p>
      <p>Lumitox is not permanent because new nerve endings grow to stimulate muscle movement again. Facial plastic surgeon Dr. Pavel Lindqvist says that many uncontrollable factors determine how long they last. Such include variability in an individual's metabolism and immune response. Both him and dermatologist Dr. Renata Olsen, however, agree on some simple ways to prolong the results.</p>
    </div>
    <span class="folio left">06</span>
  </section>

  <!-- closing page -->
  <section class="page closing">
    <p class="lead">We hope these tips will help you ride out<br>the Lumitox drought till your next appointment!</p>
    <div class="sign"><span class="dot"></span>Glow Team</div>
    <div class="band"></div>
    <div class="faint"></div>
    <div class="photo" style="left:0;top:200px;width:222px;height:205px" role="img" aria-label="Injection treatment being given near the eye"></div>
    <div class="photo dark" style="left:228px;top:200px;width:202px;height:205px" role="img" aria-label="Woman examining her face in a hand mirror"></div>
    <div class="col" style="left:22px">
      <h4>Are There Any Effective Products?</h4>
      <p class="body-text">Although plastic surgeon Dr. Claire Whitmore claims that no topical treatment can be as effective as Lumitox, she, amongst other doctors, advocate the below to help relax wrinkles: Peptides, specifically hexapeptides.</p>
    </div>
    <div class="recommend">
      <p><b>Recommended:</b><br>Verelle Firming Serum at $275<br>Collagen boosting ingredients, specifically hyaluronic acid and retinol.</p>
      <p><b>Recommended:</b><br>Lumaré Retinol Night Capsules<br>(at $33)</p>
    </div>
    <div class="col" style="left:282px">
      <h4>Is it Possible to Make Lumitox &amp; Fillers Last Longer?</h4>
      <p class="body-text">Lumitox is not permanent because new nerve endings grow to stimulate muscle movement again. Facial plastic surgeon Dr. Pavel Lindqvist says that many uncontrollable factors determine how long they last. Such include variability in an individual's metabolism and immune response. Both him and dermatologist Dr. Renata Olsen, however, agree on some simple ways to prolong the results of Lumitox.</p>
    </div>
    <div class="foot-bar"></div>
    <span class="folio right">07</span>
  </section>

</main>
</body>
</html>
```